Business Card for Web Design consulting firm

Business card designs for Web Design consulting firm

Target Market(s)

English speaking adults ages 30 - 60. Predominantly professional services eg. Doctor, Dentist

Industry/Entity Type

Consulting

Requirements
Must have
• Double sided card

```html
<!DOCTYPE html>
<html lang="en">
<head>
<meta charset="utf-8">
<title>Lumora Business Card</title>
<link rel="stylesheet" href="https://fonts.googleapis.com/css2?family=Exo+2:wght@400;700&display=swap">
<style>
  :root {
    --ink: #4d4d4d;
    --accent: #f79c25;
    --paper: #ffffff;
    --back-paper: #f4f5f7;
    --front-edge: #333333;
    --back-edge: #bbbbbb;
  }
  html, body {
    margin: 0;
    padding: 0;
    width: 857px;
    height: 1200px;
    overflow: hidden;
    background: var(--paper);
  }
  .sheet {
    position: relative;
    width: 857px;
    height: 1200px;
    font-family: "Exo 2", sans-serif;
    color: var(--ink);
  }
  .card {
    position: absolute;
    left: 107px;
    width: 643px;
    height: 386px;
    box-sizing: border-box;
  }
  .card-front {
    top: 159px;
    background: var(--paper);
    border: 1px solid var(--front-edge);
  }
  .card-back {
    top: 662px;
    background: var(--back-paper);
    border: 1px solid var(--back-edge);
    overflow: hidden;
  }
  .line {
    position: absolute;
    margin: 0;
    white-space: nowrap;
    line-height: 1;
  }
  .address {
    left: 89px;
    top: 85px;
    font-size: 19px;
    letter-spacing: 2.1px;
  }
  .phones {
    left: 94px;
    top: 116px;
    font-size: 19px;
    letter-spacing: 2.1px;
  }
  .pointer {
    left: 18px;
    top: 178px;
    font-size: 24px;
    font-weight: 700;
    letter-spacing: 1px;
  }
  .name {
    left: 88px;
    top: 170px;
    font-size: 32px;
    font-weight: 700;
    letter-spacing: 2.4px;
  }
  .email {
    left: 88px;
    top: 215px;
    font-size: 19px;
    letter-spacing: 2px;
  }
  .website {
    left: 89px;
    top: 307px;
    font-size: 17px;
    letter-spacing: 1.9px;
    color: var(--accent);
  }
  .brand {
    position: absolute;
    left: 30px;
    top: 240px;
    display: flex;
    align-items: center;
    gap: 18px;
  }
  .brand-dot {
    width: 54px;
    height: 54px;
    border-radius: 50%;
    background: var(--accent);
  }
  .brand-name {
    font-size: 72px;
    font-weight: 400;
    letter-spacing: 8px;
    line-height: 1;
    color: var(--ink);
  }
</style>
</head>
<body>
<main class="sheet">
  <section class="card card-front" aria-label="Card front">
    <p class="line address">42 Example Lane, Northgate, 5100</p>
    <p class="line phones">t. 08 5.550.1234 f. 0400555019</p>
    <span class="line pointer">&gt;&gt;</span>
    <h1 class="line name">Daniel Harper</h1>
    <p class="line email">Email: hello@lumora.co</p>
    <p class="line website">www.lumora.co</p>
  </section>

  <section class="card card-back" aria-label="Card back">
    <div class="brand">
      <span class="brand-dot"></span>
      <span class="brand-name">LUMORA</span>
    </div>
  </section>
</main>
</body>
</html>
```